Heronby Mortgage Capital Business Card

We need a business card design for our mortgage servicing company. In addition to servicing the loans of homeowners, we help homeowners with purchasing their homes and any mortgage refinancing. We would like to see designs that use the colors in the logo attached below (gold-ish yellow and navy blue), and any other design you deem fit! The design should communicate a simpler life with smart mortgages provided by Heronby.

```html
<!DOCTYPE html>
<html lang="en">
<head>
<meta charset="utf-8">
<title>Heronby Mortgage Capital – Business Card</title>
<link rel="stylesheet" href="https://fonts.googleapis.com/css2?family=Lato:wght@300;400;700&display=swap">
<style>
  :root {
    --navy: #262151;
    --gold: #e0b13c;
    --white: #ffffff;
    --backdrop: #cccccc;
  }
  * { margin: 0; padding: 0; box-sizing: border-box; }
  html, body { width: 1200px; height: 1200px; overflow: hidden; }
  body {
    background: var(--backdrop);
    position: relative;
    font-family: "Lato", Arial, sans-serif;
  }
  .card {
    position: absolute;
    left: 186px;
    width: 828px;
    height: 461px;
    background: var(--white);
    overflow: hidden;
  }
  .card--front { top: 95px; }
  .card--back { top: 644px; }
  .rule { position: absolute; left: 0; width: 100%; height: 4px; }
  .rule--navy { background: var(--navy); }
  .rule--gold { background: var(--gold); }

  .wordmark {
    position: absolute;
    left: 0; right: 0;
    top: 190px;
    text-align: center;
    font-weight: 700;
    font-size: 70px;
    letter-spacing: 1px;
    color: var(--navy);
  }

  .contact-panel {
    position: absolute;
    left: 62px; top: 0;
    width: 446px; height: 100%;
    background: var(--navy);
  }
  .contact-panel .rule--light { background: var(--white); }
  .contact-list {
    position: absolute;
    left: 33px; top: 206px;
    list-style: none;
    color: var(--white);
    font-weight: 300;
    font-size: 23px;
    line-height: 31px;
  }
  .contact-list li {
    display: flex;
    align-items: flex-start;
    margin-bottom: 6px;
  }
  .contact-icon {
    width: 19px; height: 19px;
    margin: 6px 10px 0 0;
    flex: none;
    fill: var(--gold);
  }
  .identity {
    position: absolute;
    right: 64px; top: 180px;
    text-align: right;
  }
  .identity__name {
    font-weight: 700;
    font-size: 38px;
    color: var(--navy);
    line-height: 46px;
  }
  .identity__role {
    font-weight: 300;
    font-size: 23px;
    line-height: 28px;
    color: var(--gold);
  }
</style>
</head>
<body>
  <section class="card card--front" aria-label="Card front">
    <div class="rule rule--navy" style="top:28px"></div>
    <div class="rule rule--gold" style="top:43px"></div>
    <div class="wordmark">Heronby Mortgage</div>
    <div class="rule rule--gold" style="top:413px"></div>
    <div class="rule rule--navy" style="top:428px"></div>
  </section>

  <section class="card card--back" aria-label="Card back">
    <div class="rule rule--navy" style="top:30px"></div>
    <div class="rule rule--gold" style="top:44px"></div>
    <div class="rule rule--gold" style="top:414px"></div>
    <div class="rule rule--navy" style="top:428px"></div>

    <div class="contact-panel">
      <div class="rule rule--light" style="top:30px"></div>
      <div class="rule rule--gold" style="top:44px"></div>
      <div class="rule rule--gold" style="top:414px"></div>
      <div class="rule rule--light" style="top:428px"></div>

      <ul class="contact-list">
        <li>
          <svg class="contact-icon" viewBox="0 0 20 20" aria-hidden="true"><path d="M10 0a7 7 0 0 0-7 7c0 5 7 13 7 13s7-8 7-13a7 7 0 0 0-7-7zm0 10a3 3 0 1 1 0-6 3 3 0 0 1 0 6z"/></svg>
          <span>48 Harbor Road, Suite 210,<br>Eastwick, NJ 07999</span>
        </li>
        <li>
          <svg class="contact-icon" viewBox="0 0 20 20" aria-hidden="true"><path d="M4 1l4 4-2 3c1 3 3 5 6 6l3-2 4 4-3 3C8 19 1 12 1 4z"/></svg>
          <span>(888)-555-0142</span>
        </li>
        <li>
          <svg class="contact-icon" viewBox="0 0 20 20" aria-hidden="true"><path d="M0 4h20v12H0zM1 5l9 7 9-7" stroke="#262151" stroke-width="1.4"/></svg>
          <span>sales@heronbymtg.com</span>
        </li>
        <li>
          <svg class="contact-icon" viewBox="0 0 20 20" aria-hidden="true"><path d="M3 0l13 11h-6l3 7-3 1-3-7-4 4z"/></svg>
          <span>heronbymtg.com</span>
        </li>
      </ul>
    </div>

    <div class="identity">
      <div class="identity__name">Full name</div>
      <div class="identity__role">Mortgage Agent</div>
      <div class="identity__role">License 000000000</div>
    </div>
  </section>
</body>
</html>
```